SEO marketing site

I need a design only for an SEO/Marketing project I have in mind. I have bought the domain Brivvora.example and want to aim this project at businesses who want to push their business further. WHEN I SAY DESIGN ONLY, I MEAN NO PROGRAMMING. HOWEVER, I DO NEED THE DESIGNER TO PUT THIS SITE ONLINE. $300 IS A LOT OF MONEY FOR A TEMPLATE YOU CAN PURCHASE FOR $60 WITH SOME CUSTOMISATION.

The idea is that businesses will register with us and will be offered two different kinds of services. They can make use of our scripts to check their back links, rankings, compare with competitors and a number of other marketing tools. The other service we provide is that we offer them an SEO service at a very competitive price. We will handle social networking, link building, article submission, directory submission, social bookmarking etc etc at a reasonable monthly fee.

I qoros tram look/flat design is what I really like, and I want to give off a professional vibe. This is the kind of site I wish to go for.

JUST TO REPEAT, I NEED A DESIGN TO BE PUT ONLINE, I.E PSD TO HTML CONVERSION. MY PROGRAMMERS WILL CODE THE CLIENT AREA THEMSELVES.

Target Market(s)

Other businesses

Industry/Entity Type

Marketing

Requirements
Must have
• Qoros 8 or flat design look. Even a site, similar to makerhive, is quite attractive. I would like a killer design for the site.

```html
<!DOCTYPE html>
<html lang="en">
<head>
<meta charset="utf-8">
<title>Brivvora – SEO &amp; Marketing</title>
<link rel="stylesheet" href="https://fonts.googleapis.com/css2?family=Open+Sans:wght@400;600;700&display=swap">
<style>
:root{
  --blue:#2f72c4;
  --blue-deep:#1f63b8;
  --blue-hero-a:#5ab8ec;
  --blue-hero-b:#2a6fc4;
  --orange:#e89a1f;
  --orange-btn:#f3a424;
  --text:#3c3c3c;
  --muted:#555;
  --grey-bg:#f2f2f2;
  --line:#d4d4d4;
  --white:#fff;
}
*{margin:0;padding:0;box-sizing:border-box}
html,body{width:1200px;height:2206px;overflow:hidden;background:var(--white)}
body{position:relative;font-family:"Open Sans",Arial,sans-serif;color:var(--text);font-size:13px}
.abs{position:absolute}
a{color:inherit;text-decoration:none}

/* header */
.site-header{left:0;top:0;width:1200px;height:103px;background:var(--white)}
.logo-panel{left:0;top:0;width:490px;height:140px;z-index:3}
.brand{left:213px;top:52px;font-size:36px;font-weight:600;color:var(--blue);z-index:4;letter-spacing:.5px}
.brand-dot{display:inline-block;width:10px;height:10px;background:var(--orange);margin-left:6px;vertical-align:top;margin-top:4px}
.top-links{right:192px;top:22px;font-size:13px;display:flex;align-items:center;gap:14px}
.top-links .login{color:var(--orange)}
.social{width:auto;padding:0 6px;height:24px;line-height:24px;background:#4a86c9;color:var(--white);font-size:10px;font-weight:600}
.main-nav{top:64px;left:600px;display:flex;gap:0;font-size:14px}
.main-nav a{display:block;padding:0 18px;color:#333}
.main-nav a.active{color:var(--blue)}

/* hero */
.hero{left:0;top:103px;width:1200px;height:371px;background:radial-gradient(ellipse at 70% 10%,var(--blue-hero-a) 0%,#3b8fd6 35%,var(--blue-hero-b) 80%)}
.hero-title{left:174px;width:340px;top:188px;text-align:right;color:var(--white);font-size:21px;font-weight:400}
.hero-title::after{content:" ›";color:#9fd3f5}
.hero-rule{left:174px;top:226px;width:360px;height:1px;background:rgba(255,255,255,.55)}
.hero-copy{left:174px;top:242px;width:360px;text-align:center;color:var(--white);font-size:12.5px;line-height:17px}
.hero-copy p+p{margin-top:12px}
.btn-register{left:405px;top:383px;width:126px;height:33px;border-radius:6px;background:linear-gradient(#f4f4f4,#bfc6cc);color:var(--blue-deep);font-weight:600;font-size:15px;text-align:center;line-height:33px;box-shadow:0 1px 3px rgba(0,0,0,.3)}
.hero-visual{left:588px;top:150px;width:425px;height:282px;border-radius:6px;background:linear-gradient(135deg,#fafafa,#d9dde2);box-shadow:0 6px 18px rgba(0,0,0,.25)}
.slider-dots{left:554px;top:494px;display:flex;gap:8px}
.slider-dots span{width:14px;height:14px;border-radius:50%;border:2px solid #9bc3e6;background:var(--white)}
.slider-dots span.on{background:#3d7fc0;border-color:#b8d2ea}

/* services */
.service{width:300px;text-align:center}
.service h3{font-size:18px;font-weight:400;color:var(--blue)}
.service .thumb{width:108px;height:108px;border-radius:50%;margin:18px auto 0;border:4px solid #f3e1c4}
.service p{margin:20px auto 0;width:250px;font-size:12.5px;line-height:17px;color:var(--text)}
.btn-read{display:block;margin:20px auto 0;width:90px;height:27px;line-height:27px;background:#dedede;border:1px solid #c8c8c8;font-size:12px;color:#444}

/* sections */
.band-grey{left:0;width:1200px;background:var(--grey-bg);border-top:1px solid var(--line)}
.band-white{left:0;width:1200px;background:var(--white);border-top:1px solid var(--line)}
.section-title{font-size:19px;font-weight:400;color:var(--blue)}
.section-sub{font-size:14px;color:var(--orange);display:flex;align-items:center;gap:12px}
.section-sub::after{content:"";flex:1;border-top:2px dotted #ccc}
.copy{font-size:12.5px;line-height:17px;color:var(--text);text-align:justify}
.copy p+p{margin-top:12px}
.btn-know{height:33px;line-height:33px;width:98px;background:var(--orange-btn);color:var(--white);font-weight:600;font-size:14px;text-align:center;border:1px solid #e2901a}
.ticks{list-style:none}
.ticks li{position:relative;padding-left:18px;font-size:12.5px;line-height:17px;text-align:justify;margin-bottom:10px}
.ticks svg{position:absolute;left:0;top:3px}

.monitor-visual{left:152px;top:960px;width:322px;height:267px;background:linear-gradient(#2b2b2b 0,#2b2b2b 70%,#cfcfcf 70%,#e9e9e9 100%);border-radius:4px}
.phone-visual{left:786px;top:1356px;width:199px;height:260px;background:linear-gradient(90deg,#1e1e1e 0,#2c2c2c 55%,#eeeeee 65%,#f7f7f7 100%);border-radius:18px 6px 6px 18px}
.person-visual{left:202px;top:1712px;width:193px;height:301px;background:linear-gradient(#e9d2b8 0,#c99b6c 35%,#6d6e72 60%,#4a4b50 100%);border-radius:90px 90px 0 0}

.cta{left:0;top:2013px;width:1200px;height:101px;background:#fafafa;border-top:1px solid var(--line);text-align:center;line-height:101px;font-size:15px;color:#444}
.cta strong{color:var(--blue-deep)}
.site-footer{left:0;top:2114px;width:1200px;height:92px;background:var(--grey-bg)}
.footer-nav{left:152px;top:36px;font-size:12.5px;color:#444}
.footer-nav a.active{color:var(--blue)}
.footer-nav span{margin:0 9px;color:#777}
.copyright{right:160px;top:36px;font-size:12.5px;color:#444}
</style>
</head>
<body>

<header class="site-header abs">
  <nav class="top-links abs">
    <a class="login" href="#">Login</a>
    <a href="#">Register</a>
    <span>|</span>
    <span class="social">Chirply</span>
    <span class="social">Friendbook</span>
  </nav>
  <nav class="main-nav abs">
    <a class="active" href="#">Home</a>
    <a href="#">About Us</a>
    <a href="#">Services</a>
    <a href="#">Advance Tool</a>
    <a href="#">Contact Us</a>
  </nav>
</header>

<section class="hero abs">
</section>
<svg class="logo-panel abs" viewBox="0 0 490 140" width="490" height="140">
  <polygon points="0,0 482,0 403,137 0,137" fill="#fff"/>
  <line x1="482" y1="0" x2="403" y2="137" stroke="#2a6fc4" stroke-width="4"/>
</svg>
<div class="brand abs">Brivvora<span class="brand-dot"></span></div>

<h1 class="hero-title abs">Welcome to our site</h1>
<div class="hero-rule abs"></div>
<div class="hero-copy abs">
  <p>Ut enim ad minim veniam, quis nostrud exercitation ullamco laboris nisi ut aliquip ex ea commodo consequat. Duis aute irure dolor in reprehenderit in voluptate velit esse cillum dolore eu fugiat nulla pariatur.</p>
  <p>Excepteur sint occaecat cupidatat non proident, sunt in culpa qui officia deserunt mollit anim id est laborum.</p>
</div>
<a class="btn-register abs" href="#">Register Now</a>
<div class="hero-visual abs" role="img" aria-label="Tilted screen showing an SEO ranking dashboard with coloured service rows and a rising 3D bar chart"></div>

<div class="slider-dots abs"><span class="on"></span><span></span><span></span></div>

<article class="service abs" style="left:100px;top:540px">
  <h3>SEO</h3>
  <div class="thumb" role="img" aria-label="Globe resting on a keyboard" style="background:radial-gradient(circle at 50% 40%,#7fc3ee,#2a5e96 60%,#3c3c3c)"></div>
  <p>Lorem ipsum dolor sit amet, consectetur adipisicing elit, sed do eiusmod tempor</p>
  <a class="btn-read" href="#">Read More</a>
</article>
<article class="service abs" style="left:435px;top:540px">
  <h3>Lead Generation</h3>
  <div class="thumb" role="img" aria-label="Hand drawing a rising blue arrow" style="background:radial-gradient(circle at 55% 45%,#ffffff,#dfe9f3 55%,#c9b7a6)"></div>
  <p>Lorem ipsum dolor sit amet, consectetur adipisicing elit, sed do eiusmod tempor</p>
  <a class="btn-read" href="#">Read More</a>
</article>
<article class="service abs" style="left:799px;top:540px">
  <h3>Social Marketting</h3>
  <div class="thumb" role="img" aria-label="Finger touching a glowing network of contacts" style="background:radial-gradient(circle at 50% 50%,#e38b3a,#5a3a26 45%,#151515)"></div>
  <p>Lorem ipsum dolor sit amet, consectetur adipisicing elit, sed do eiusmod tempor</p>
  <a class="btn-read" href="#">Read More</a>
</article>

<section class="band-grey abs" style="top:884px;height:408px"></section>
<div class="monitor-visual abs" role="img" aria-label="Desktop monitor displaying an analytics dashboard with line and pie charts"></div>
<h2 class="section-title abs" style="left:533px;top:955px">Our Unique System</h2>
<div class="section-sub abs" style="left:533px;top:987px;width:507px">To build your market space</div>
<ul class="ticks abs" style="left:537px;top:1027px;width:488px">
  <li><svg width="12" height="10" viewBox="0 0 12 10"><path d="M1 5l3.5 3.5L11 1" fill="none" stroke="#2f72c4" stroke-width="2"/></svg>Lorem ipsum dolor sit amet, consectetur adipisicing elit, sed do eiusmod tempor incididunt ut labore et dolore magna aliqua.</li>
  <li><svg width="12" height="10" viewBox="0 0 12 10"><path d="M1 5l3.5 3.5L11 1" fill="none" stroke="#2f72c4" stroke-width="2"/></svg>Lorem ipsum dolor sit amet, consectetur adipisicing elit, sed do eiusmod tempor incididunt ut labore et dolore magna aliqua.</li>
  <li><svg width="12" height="10" viewBox="0 0 12 10"><path d="M1 5l3.5 3.5L11 1" fill="none" stroke="#2f72c4" stroke-width="2"/></svg>Lorem ipsum dolor sit amet, consectetur adipisicing elit, sed do eiusmod tempor incididunt ut labore et dolore magna aliqua.</li>
</ul>
<a class="btn-know abs" href="#" style="left:539px;top:1173px">Know More</a>

<section class="band-white abs" style="top:1292px;height:376px"></section>
<h2 class="section-title abs" style="left:152px;top:1352px">Satisfactory Services</h2>
<div class="section-sub abs" style="left:152px;top:1383px;width:525px">365/24 Days Online Helpdesk</div>
<div class="copy abs" style="left:152px;top:1421px;width:499px">
  <p>Lorem ipsum dolor sit amet, consectetur adipisicing elit, sed do eiusmod tempor incididunt ut labore et dolore magna aliqua. Ut enim ad minim veniam, quis nostrud exercitation ullamco laboris nisi ut aliquip ex ea commodo consequat. Duis aute irure dolor in reprehenderit in voluptate velit esse cillum dolore eu fugiat nulla pariatur.</p>
  <p>Excepteur sint occaecat cupidatat non proident, sunt in culpa qui officia deserunt mollit anim id est laborum.</p>
</div>
<a class="btn-know abs" href="#" style="left:152px;top:1560px">Know More</a>
<div class="phone-visual abs" role="img" aria-label="Smartphone showing a list of reports beside a sketched doodle pattern"></div>

<section class="band-grey abs" style="top:1668px;height:345px"></section>
<div class="person-visual abs" role="img" aria-label="Portrait of a smiling businesswoman in a grey blazer"></div>
<h2 class="section-title abs" style="left:517px;top:1717px">Who we are</h2>
<div class="section-sub abs" style="left:517px;top:1749px;width:523px">Know about us to begin with</div>
<div class="copy abs" style="left:517px;top:1786px;width:500px">
  <p>Lorem ipsum dolor sit amet, consectetur adipisicing elit, sed do eiusmod tempor incididunt ut labore et dolore magna aliqua. Ut enim ad minim veniam, quis nostrud exercitation ullamco laboris nisi ut aliquip ex ea commodo consequat. Duis aute irure dolor in reprehenderit in voluptate velit esse cillum dolore eu fugiat nulla pariatur.</p>
  <p>Excepteur sint occaecat cupidatat non proident, sunt in culpa qui officia deserunt mollit anim id est laborum.</p>
</div>
<a class="btn-know abs" href="#" style="left:517px;top:1930px">Know More</a>

<section class="cta abs">To give your business a boost of progress with us, <strong>Register Now.</strong></section>

<footer class="site-footer abs">
  <nav class="footer-nav abs">
    <a class="active" href="#">Home</a><span>|</span><a href="#">About Us</a><span>|</span><a href="#">Services</a><span>|</span><a href="#">Advance Tool</a><span>|</span><a href="#">Contact Us</a>
  </nav>
  <div class="copyright abs">Copyright@2013, brivvora SEO</div>
</footer>

</body>
</html>
```